The Nine Gates for Tablet Reliance - Contemporary Book Cover Design

The Nine Gates for Tablet Reliance was published in March 2019 and is available on Brimora and other platforms now. However, I am not happy with the cover.  It's a good design in some ways - I thought it would stand out and be easily recognizable. But I don't really like the color scheme and feel that a self-help book should probably use some lighter colors and that the red is too strident. The color scheme carries over into other marketing materials like the website, social media, etc. and I don't like the red and black scheme for these purposes.
It's not essential that the cover contain an endorsement like the current one but it could. Here are some endorsements:
“A must-read for anyone who is addicted to or thinks they may have a problem with digital technology. This eloquent work will also be useful to academics and clinicians exploring potential solutions. The author recognizes the similarities between smartphone addiction and other addictions, and logically applies one of the most effective known solutions for addiction - The Nine Gates.”
-- Dale Wickersham: Noted Interventionist, Keynote Speaker and Addiction Visionary
“If you suffer from digital addiction, I strongly encourage you to use this book as your road map to get you back to the real world.”
-- Thomas Quillard, Founder of Online Channel Monitor.
The back cover would have the new design / color scheme, but can have similar text, bio, author image, etc. Or we could include the endorsements there and shorten the other text.
As for the cover it could be stylized, or an image, a partial image, or whatever. I am open to suggestions. Think about what would be inviting for a person searching for help with moderating their smartphone use.
Let's add a subtitle as well "An Inner Journey to Balanced Tablet Habits"
Here is a link to the book:
https://www.brimora.example/Nine-Gates-Tablet-Reliance/dp/4086213590

Target Market(s)
General, since this issue affects almost everyone.
Colors
Designer to choose colors to be used in the design.
Look and feel

```html
<!DOCTYPE html>
<html lang="en">
<head>
<meta charset="utf-8">
<title>The Nine Gates for Tablet Reliance — Cover</title>
<link rel="stylesheet" href="https://fonts.googleapis.com/css2?family=Oswald:wght@600;700&family=Mulish:wght@500&display=swap">
<style>
  :root {
    --backdrop: #9cc6a3;
    --cover-light: #e9e8e6;
    --ink-navy: #2b3444;
    --green-deep: #3f9a66;
    --green-bright: #3dcb6c;
    --green-muted: #6f9a80;
    --violet: #b23ad0;
    --photo-light: #6a7482;
    --photo-dark: #343f50;
    --text-light: #f1f1ef;
  }
  html, body {
    margin: 0;
    width: 1200px;
    height: 1131px;
    overflow: hidden;
    background: var(--backdrop);
  }
  .book-cover {
    position: absolute;
    left: 220px;
    top: 33px;
    width: 760px;
    height: 1064px;
    overflow: hidden;
    background: var(--cover-light);
  }
  .cover-field {
    position: absolute;
    inset: 0;
    clip-path: polygon(0 315px, 100% 196px, 100% 100%, 0 100%);
    background:
      radial-gradient(ellipse 300px 340px at 370px 600px, rgba(178, 58, 208, 0.95), rgba(140, 110, 150, 0.55) 55%, rgba(120, 140, 130, 0) 85%),
      linear-gradient(175deg, var(--green-muted) 0%, var(--green-deep) 45%, var(--green-bright) 100%);
  }
  .photo-area {
    position: absolute;
    inset: 0;
  }
  .title-block {
    position: absolute;
    left: 0;
    top: 0;
    width: 100%;
    height: 360px;
    transform: rotate(-4deg);
    transform-origin: 50% 50%;
    font-family: "Oswald", "Arial Narrow", sans-serif;
    font-weight: 700;
    text-transform: uppercase;
  }
  .title-line {
    position: absolute;
    margin: 0;
    line-height: 1;
    white-space: nowrap;
    color: var(--ink-navy);
  }
  .title-article { left: 300px; top: 40px; font-size: 50px; }
  .title-main { left: 122px; top: 92px; font-size: 96px; letter-spacing: 3px; }
  .title-joiner { left: 330px; top: 212px; font-size: 50px; }
  .title-topic { left: 118px; top: 276px; font-size: 68px; letter-spacing: 2px; color: var(--text-light); }
  .subtitle {
    position: absolute;
    left: 430px;
    top: 565px;
    width: 290px;
    margin: 0;
    transform: rotate(-11deg);
    font-family: "Mulish", "Helvetica", sans-serif;
    font-weight: 500;
    font-size: 36px;
    line-height: 1.2;
    text-align: center;
    color: var(--text-light);
  }
  .author {
    position: absolute;
    left: 0;
    width: 710px;
    bottom: 8px;
    margin: 0;
    font-family: "Oswald", "Arial Narrow", sans-serif;
    font-weight: 600;
    font-size: 46px;
    letter-spacing: 2px;
    text-transform: uppercase;
    text-align: center;
    color: var(--text-light);
  }
</style>
</head>
<body>
  <main class="book-cover">
    <div class="cover-field"></div>

    <svg class="photo-area" width="760" height="1064" viewBox="0 0 760 1064" role="img" aria-label="Photograph of a hand holding a phone with a dark screen">
      <defs>
        <linearGradient id="photoTone" x1="0" y1="0" x2="1" y2="1">
          <stop offset="0" stop-color="var(--photo-light)"/>
          <stop offset="1" stop-color="var(--photo-dark)"/>
        </linearGradient>
      </defs>
      <rect x="405" y="340" width="400" height="780" rx="40" fill="url(#photoTone)" transform="rotate(-11 605 730)"/>
    </svg>

    <header class="title-block">
      <h1 class="title-line title-article">The</h1>
      <p class="title-line title-main">Nine Gates</p>
      <p class="title-line title-joiner">For</p>
      <p class="title-line title-topic">Tablet Reliance</p>
    </header>

    <p class="subtitle">An Inner Journey to Balanced Tablet Habits</p>

    <p class="author">Owen Marlock</p>
  </main>
</body>
</html>
```